Vellora Trae - flyer for launch of new App with Web platform & Beacon support

Create an e-flyer for the new launch of Museum Web / App / Beacon platform for museum content delivery, management, experience and analytics.
The features of the product are contained in the pdf file uploaded for content and style guidance.
The e-flyer will be used as a mail drop and at conference events.

Target Market(s)

Museum owners, curators, innovation departments and potential sponsors.

Industry/Entity Type

Museum

Font styles to use
Other font styles liked:
• Presentation DIN Alternate or similar

Requirements
Must have
• Clear value proposition.
Nice to have
• Simple smart beacon explanation on how the technology links together.
• Web platform provides content management data to the App which then communicates with beacons located strategically inside the museum and relates to the user settings in the App (age, language, interests) to create a targeted experience.
Should not have
• Complexity and a lot of wording.

```html
<!DOCTYPE html>
<html lang="en">
<head>
<meta charset="utf-8">
<title>Vellora Trae – Launch Flyer</title>
<link rel="stylesheet" href="https://fonts.googleapis.com/css2?family=Barlow:wght@300;400;700&display=swap">
<style>
  :root {
    --stage: #00a5ea;
    --paper: #ffffff;
    --ink: #000000;
    --accent: #0aa2e6;
    --text-light: #e9e9e9;
    --text-muted: #cfcfcf;
    --ring: #8a8a8a;
  }
  * { margin: 0; padding: 0; box-sizing: border-box; }
  html, body { width: 1200px; height: 1153px; overflow: hidden; }
  body {
    background: var(--stage);
    font-family: "Barlow", "Helvetica Neue", Arial, sans-serif;
    position: relative;
  }
  .flyer {
    position: absolute;
    left: 255px; top: 26px;
    width: 689px; height: 1100px;
    background: var(--ink);
    overflow: hidden;
  }
  .flyer__top {
    position: absolute; left: 0; top: 0;
    width: 100%; height: 262px;
    background: var(--paper);
  }
  .brand-disc {
    position: absolute;
    left: 238px; top: 121px;
    width: 250px; height: 250px;
    border-radius: 50%;
    background: var(--ink);
    border: 1px solid var(--ring);
    display: flex; align-items: center; justify-content: center;
  }
  .brand-disc__name {
    color: var(--paper);
    font-weight: 300;
    font-size: 26px;
    letter-spacing: 3px;
    text-transform: uppercase;
  }
  .intro {
    position: absolute; left: 218px;
    color: var(--text-light);
    font-weight: 300;
    font-size: 22px;
    line-height: 31.6px;
    text-transform: uppercase;
    letter-spacing: 0.3px;
  }
  .intro--past { top: 399px; }
  .intro--tech { top: 510px; }
  .headline {
    position: absolute; left: 218px; top: 596px;
    color: var(--accent);
    font-weight: 700;
    font-size: 42px;
    line-height: 40px;
    text-transform: uppercase;
    letter-spacing: -0.3px;
  }
  .features {
    position: absolute; left: 221px; top: 772px;
    list-style: none;
    color: var(--text-muted);
    font-weight: 400;
    font-size: 14.5px;
    line-height: 20.6px;
    letter-spacing: 0.8px;
    text-transform: uppercase;
  }
  .offer {
    position: absolute; left: 52px; top: 908px;
    color: var(--accent);
    font-weight: 700;
    text-transform: uppercase;
    line-height: 1;
  }
  .offer__price { font-size: 34px; }
  .offer__price sup { font-size: 10px; vertical-align: top; }
  .offer__period { font-size: 22px; margin-top: 0; }
  .offer__launch { font-size: 22px; margin-top: 16px; line-height: 19px; }
  .gallery {
    position: absolute; left: 221px; top: 906px;
    width: 468px; height: 126px;
    display: flex; gap: 2px;
    background: var(--accent);
  }
  .gallery__tile { flex: 1; height: 100%; }
  .gallery__tile--cms { background: linear-gradient(135deg, #eef0f4, #c9cfdc 60%, #5a6fb0); }
  .gallery__tile--visitor { background: linear-gradient(160deg, #f1efe9, #b8b4aa 55%, #6f6a62); }
  .gallery__tile--phone { background: linear-gradient(90deg, #e8e6e0 0%, #1a1a1a 20%, #111 55%, #d9d6cf 75%, #4f7fb8 100%); }
  .gallery__tile--watch { background: linear-gradient(150deg, #d8dde3, #a8b0ba 50%, #4a4f57); }
  .footnote {
    position: absolute; left: 221px; top: 1040px;
    color: var(--text-muted);
    font-size: 13px;
    letter-spacing: 1px;
    text-transform: uppercase;
  }
</style>
</head>
<body>
  <main class="flyer">
    <div class="flyer__top"></div>
    <div class="brand-disc"><span class="brand-disc__name">Vellora Trae</span></div>

    <p class="intro intro--past">Museums anchor us to the past,<br>question our present and<br>pull us into the future</p>
    <p class="intro intro--tech">While technology opens our<br>world to new possibilities</p>

    <h1 class="headline">Now Vellora Trae<br>brings you both in a<br>brilliantly simple<br>open platform</h1>

    <ul class="features">
      <li>Content web preparation &amp; management</li>
      <li>Smartphone / tablet app delivery</li>
      <li>Smart beacon dynamic reality positioning</li>
      <li>Wearables push messaging</li>
      <li>Augmented reality enhancement</li>
      <li>Incredible access pricing</li>
    </ul>

    <div class="offer">
      <div class="offer__price">$500<sup>*</sup></div>
      <div class="offer__period">Per month</div>
      <div class="offer__launch">Launching<br>soon</div>
    </div>

    <div class="gallery">
      <div class="gallery__tile gallery__tile--cms" role="img" aria-label="Keyboard with a content management system key"></div>
      <div class="gallery__tile gallery__tile--visitor" role="img" aria-label="Museum visitor holding a tablet in a gallery"></div>
      <div class="gallery__tile gallery__tile--phone" role="img" aria-label="Hand holding a smartphone showing a beacon signal"></div>
      <div class="gallery__tile gallery__tile--watch" role="img" aria-label="Wrist wearing a smartwatch in a busy hall"></div>
    </div>

    <p class="footnote">*Basic visitor package - no smart beacons investment</p>
  </main>
</body>
</html>
```